Corvella Back & Joint 3 Fold Brochure

Create a eye catchy brochure about the partnership between chiropractors and Corvella Back & Joint and Veltrana to use as leave behind for our marketing reps to use. I have uploaded the content. a sample of the CBJ brochure we use as inspiration and colors and logos

```html
<!DOCTYPE html>
<html lang="en">
<head>
<meta charset="UTF-8">
<title>Corvella Back &amp; Joint – Chiropractic Partnership Tri-fold</title>
<link href="https://fonts.googleapis.com/css2?family=Montserrat:wght@300;400;500;700;800;900&display=swap" rel="stylesheet">
<style>
  :root{
    --teal:#1f9483;
    --teal-deep:#167a6c;
    --aqua:#2ec4b6;
    --ink:#1d2b2a;
    --paper:#ffffff;
    --bg:#f1f2f2;
  }
  *{box-sizing:border-box;margin:0;padding:0}
  html,body{width:1200px;height:800px;overflow:hidden;background:var(--bg)}
  body{font-family:'Montserrat',sans-serif;color:var(--ink)}
  .brochure{display:flex;width:1200px;height:800px}
  .panel{width:400px;height:800px;position:relative;overflow:hidden}

  /* about panel */
  .panel-about{background:var(--teal);color:#fff;padding:38px 34px 0}
  .about-kicker{font-size:24px;font-weight:400;line-height:1.1}
  .about-title{font-size:26px;font-weight:800;line-height:1.15;margin-bottom:10px}
  .about-text{font-size:12px;line-height:1.4;margin-bottom:10px;font-weight:400}
  .benefits-title{font-size:26px;font-weight:800;margin:16px 0 8px;line-height:1.1}
  .benefit{display:flex;gap:12px;align-items:flex-start;margin-bottom:8px;position:relative;z-index:1}
  .benefit svg{flex:none;margin-top:12px}
  .benefit h4{font-size:12.5px;font-weight:800;line-height:1.2}
  .benefit p{font-size:13px;line-height:1.25}
  .photo{position:absolute;left:0;right:0;bottom:0;height:220px;
    background:linear-gradient(180deg,var(--teal) 0%,#5f8f8a 25%,#9fb3b1 55%,#6d7f6a 100%)}

  /* service panels */
  .panel-services{background:var(--paper)}
  .services-band{position:absolute;left:0;top:0;width:400px;height:150px}
  .services-heading{position:absolute;left:34px;top:40px;color:#fff;font-size:32px;font-weight:900;letter-spacing:.5px}
  .intro{position:absolute;left:40px;top:150px;right:30px;color:var(--teal)}
  .intro h2{font-size:19px;font-weight:800;margin-bottom:4px}
  .intro p{font-size:12.5px;line-height:1.3}
  .service-list{position:absolute;left:0;right:0;padding:0 24px 0 30px}
  .service{display:flex;gap:14px;align-items:flex-start;margin-bottom:18px}
  .service-icon{flex:none;width:80px;display:flex;justify-content:center;padding-top:20px}
  .service h3{font-size:17px;font-weight:800;color:var(--aqua);line-height:1.05;padding-bottom:4px;border-bottom:2px solid var(--aqua);margin-bottom:5px}
  .service p{font-size:12px;line-height:1.3}
</style>
</head>
<body>
<main class="brochure">

  <section class="panel panel-about">
    <p class="about-kicker">Georgia's Largest</p>
    <h1 class="about-title">Relief Provider</h1>
    <p class="about-text">Chiropractors and Corvella Back &amp; Joint now work side by side. Together with Veltrana, our dedicated team of seasoned healthcare professionals brings extensive expertise in pain and spine care, so your patients receive the highest standard of medical attention. With precision diagnostics and compassionate care, we support every chiropractic plan on the journey to optimal health.</p>
    <p class="about-text">Our doctors represent our dedication to your patients' well-being. Each professional within our team is chosen for proficiency, empathy, and commitment to exceptional care, reflecting each of our values to the highest degree.</p>
    <h2 class="benefits-title">Benefits</h2>
    <div class="benefit">
      <svg width="22" height="22" viewBox="0 0 22 22"><circle cx="11" cy="11" r="11" fill="#fff"/><path d="M8 6l8 5-8 5z" fill="var(--teal)"/></svg>
      <div><h4>Transportation Offered</h4><p>Effortless health journeys with transport provided.</p></div>
    </div>
    <div class="benefit">
      <svg width="22" height="22" viewBox="0 0 22 22"><circle cx="11" cy="11" r="11" fill="#fff"/><path d="M8 6l8 5-8 5z" fill="var(--teal)"/></svg>
      <div><h4>Bilingual Staff</h4><p>Our fluent bilingual team ensures clear communication for all patients.</p></div>
    </div>
    <div class="photo" role="img" aria-label="Photo of a doctor with a tablet talking with two senior patients in a bright clinic"></div>
  </section>

  <section class="panel panel-services">
    <svg class="services-band" viewBox="0 0 400 150" aria-hidden="true">
      <path d="M0 0H400V70Q220 90 0 150Z" fill="var(--teal)"/>
      <path d="M0 150Q220 92 400 70V82Q220 100 0 150Z" fill="var(--teal-deep)" opacity=".6"/>
    </svg>
    <h1 class="services-heading">OUR SERVICES</h1>
    <div class="intro">
      <h2>Our Methods In Healing</h2>
      <p>Discover cutting-edge pain and spine care, from targeted injections and advanced therapies to non-invasive imaging—all designed for your optimal well-being.</p>
    </div>
    <div class="service-list" style="top:262px">
      <article class="service">
        <div class="service-icon"><svg width="40" height="80" viewBox="0 0 40 80"><path d="M12 4C30 20 6 40 24 76" stroke="var(--aqua)" stroke-width="8" fill="none" stroke-dasharray="4 3"/></svg></div>
        <div><h3>Epidural Spinal<br>Injections</h3><p>Swiftly deliver pain relief with epidural corticosteroid injections. Targeting the epidural area shields the spinal cord, easing discomfort efficiently.</p></div>
      </article>
      <article class="service">
        <div class="service-icon"><svg width="70" height="70" viewBox="0 0 70 70" stroke="var(--aqua)" stroke-width="3" fill="var(--aqua)"><path d="M35 35L8 18M35 35L62 14M35 35L10 50M35 35L56 60M35 35L30 64M35 35L40 6"/><circle cx="8" cy="18" r="4"/><circle cx="62" cy="14" r="4"/><circle cx="10" cy="50" r="4"/><circle cx="56" cy="60" r="4"/><circle cx="30" cy="64" r="4"/><circle cx="40" cy="6" r="4"/><circle cx="35" cy="35" r="5"/></svg></div>
        <div><h3>Nerve Root<br>Blocks</h3><p>Combat arm or leg pain with nerve root blocks. Precision injections under X-ray guidance alleviate discomfort along the nerve's path.</p></div>
      </article>
      <article class="service">
        <div class="service-icon"><svg width="72" height="56" viewBox="0 0 72 56" fill="none" stroke="var(--aqua)" stroke-width="2"><rect x="2" y="2" width="68" height="52" rx="3"/><ellipse cx="38" cy="27" rx="18" ry="14"/><path d="M38 13v28M26 22q6 4 12 0M40 30q6 4 12 0M8 14h10M8 20h8M8 44h12"/></svg></div>
        <div><h3>Fluoroscopy</h3><p>Experience live X-ray imaging with fluoroscopy. Real-time views aid orthopedic diagnoses, surgery, and procedures, offering dynamic insights.</p></div>
      </article>
      <article class="service">
        <div class="service-icon"><svg width="64" height="64" viewBox="0 0 64 64" fill="none" stroke="var(--aqua)"><circle cx="32" cy="32" r="28" stroke-width="1" opacity=".4"/><circle cx="32" cy="32" r="22" stroke-width="1.5" opacity=".6"/><circle cx="32" cy="32" r="15" stroke-width="2"/><circle cx="32" cy="32" r="8" fill="var(--aqua)" stroke="none"/></svg></div>
        <div><h3>Trigger Point<br>Injections</h3><p>Address muscle knots causing pain with trigger point injections. This procedure targets muscle trigger points, relieving pain and promoting relaxation.</p></div>
      </article>
    </div>
  </section>

  <section class="panel panel-services">
    <div class="service-list" style="top:40px">
      <article class="service">
        <div class="service-icon"><svg width="40" height="70" viewBox="0 0 40 70" fill="var(--aqua)"><path d="M20 68C10 50 30 36 18 20" stroke="var(--aqua)" stroke-width="3" fill="none"/><ellipse cx="10" cy="14" rx="5" ry="10" transform="rotate(-25 10 14)"/><ellipse cx="28" cy="10" rx="4" ry="9" transform="rotate(25 28 10)"/><ellipse cx="30" cy="40" rx="4" ry="8" transform="rotate(50 30 40)"/></svg></div>
        <div><h3>Transforaminal<br>Injections</h3><p>Relieve lower back, leg, and sciatica pain with transforaminal injections. Targeted steroid medication reduces inflammation along the spinal nerve roots.</p></div>
      </article>
      <article class="service">
        <div class="service-icon"><svg width="50" height="66" viewBox="0 0 50 66" fill="none" stroke="var(--aqua)" stroke-width="3"><path d="M12 26h16l-4 22h-8zM20 48v14"/><path d="M30 14q8 4 8 12M34 6q12 6 12 20"/></svg></div>
        <div><h3>Ultrasound</h3><p>Opt for comfortable orthopedic imaging with ultrasound. Radiation-free, affordable, and patient-friendly, ultrasounds provide clear diagnostics without inconvenience.</p></div>
      </article>
      <article class="service">
        <div class="service-icon"><svg width="70" height="40" viewBox="0 0 70 40" fill="none" stroke="var(--aqua)" stroke-width="2"><path d="M2 22h12l4-10 4 20 4-28 4 32 4-24 4 16 4-10 4 6h20"/></svg></div>
        <div><h3>Radiofrequency<br>Ablation</h3><p>Minimize tumors and chronic pain with radiofrequency ablation. This minimally invasive technique is effective for various conditions, ensuring relief.</p></div>
      </article>
      <article class="service">
        <div class="service-icon"><svg width="44" height="72" viewBox="0 0 44 72" fill="var(--aqua)"><circle cx="8" cy="6" r="3"/><circle cx="12" cy="16" r="4"/><circle cx="20" cy="26" r="5"/><circle cx="30" cy="34" r="5"/><path d="M34 44q6 14-4 26" stroke="var(--aqua)" stroke-width="3" fill="none"/></svg></div>
        <div><h3>Spinal Cord<br>Stimulation</h3><p>Implant spinal cord stimulators for pain relief. Low-level electrical signals block pain signals, replacing them with soothing sensations for comfort.</p></div>
      </article>
      <article class="service">
        <div class="service-icon"><svg width="56" height="56" viewBox="0 0 56 56" fill="none" stroke="var(--aqua)" stroke-width="4"><path d="M10 34V28a18 18 0 0 1 36 0v6"/><rect x="6" y="30" width="10" height="16" rx="4" fill="var(--aqua)"/><rect x="40" y="30" width="10" height="16" rx="4" fill="var(--aqua)"/><path d="M45 46q0 6-10 6h-4"/></svg></div>
        <div><h3>TeleMed<br>Follow-Ups</h3><p>Accessible care with TeleMed follow-ups. Conveniently receive post-procedure assessments and appointments from the comfort of your home. Prioritize recovery without travel hassles.</p></div>
      </article>
    </div>
  </section>

</main>
</body>
</html>
```